Switch Kit - Banking Flyer

We want a design for an 8.5x11" flyer that matches the look of our website (www.morvalecommercebank.com). Outline is attached, but please feel free to include images/pictures/graphics that you think makes this easy to understand. The goal is to hand this flyer to a potential customer to get them to understand the information easily and quickly.

```html
<!DOCTYPE html>
<html lang="en">
<head>
<meta charset="utf-8">
<title>Switch Kit Flyer – Morvale Commerce Bank</title>
<link rel="stylesheet" href="https://fonts.googleapis.com/css2?family=Montserrat:ital,wght@0,400;0,600;0,700;1,400&family=Oswald:wght@500&display=swap">
<style>
:root{
  --gold:#a8731f;
  --navy:#34486a;
  --paper:#f7f7f8;
  --light:#e9ebee;
  --ink:#2f3b52;
  --muted:#5d6473;
  --white:#ffffff;
  --stage:#5b5f64;
  --photo-sky:#8fa7b8;
  --photo-stone:#c9a590;
  --photo-brick:#9a5a45;
}
*{margin:0;padding:0;box-sizing:border-box}
html,body{width:1200px;height:853px;overflow:hidden}
body{background:var(--stage);font-family:'Montserrat',sans-serif;color:var(--ink)}
.flyer{position:absolute;left:290px;top:25px;width:620px;height:802px;background:var(--paper);overflow:hidden}
.brand{position:absolute;left:34px;top:44px;display:flex;align-items:center;gap:8px}
.brand-mark{width:14px;height:14px;background:var(--gold)}
.brand-name{font-weight:700;font-size:17px;color:var(--gold);letter-spacing:.5px}
.hero-photo{position:absolute;left:300px;top:34px;width:300px;height:250px;
  clip-path:polygon(30px 0,100% 0,100% 100%,30px 100%,0 calc(100% - 30px),0 30px);
  background:linear-gradient(180deg,var(--photo-sky) 0%,var(--photo-sky) 32%,var(--photo-stone) 42%,var(--photo-brick) 78%,#4b5a46 100%)}
.hero-frame{position:absolute;left:0;top:0;width:620px;height:360px;pointer-events:none}
.hero-tag{position:absolute;right:20px;top:248px;width:170px;background:var(--gold);color:var(--white);
  font-family:'Oswald',sans-serif;font-size:9px;line-height:1.25;text-align:right;padding:6px 10px 6px 16px;
  clip-path:polygon(12px 0,100% 0,100% 100%,0 100%)}
.intro{position:absolute;left:30px;top:140px;width:330px;height:200px;color:var(--white);
  font-family:'Oswald',sans-serif;font-weight:500;font-size:14.5px;line-height:1.28;padding:18px 40px 0 18px}
.intro p+p{margin-top:14px}
.intro .intro-lead{font-size:13.5px}

.flyer-body{position:absolute;left:0;top:360px;bottom:0;width:620px;display:flex;flex-direction:column}
.step{padding:0 40px}
.step h2{font-size:15.5px;font-weight:700;line-height:1.15;color:var(--navy)}
.step p{font-size:10px;line-height:1.3;margin-top:4px;color:var(--muted)}
.step-one{padding-top:6px;padding-bottom:12px}
.step-two{background:var(--navy);padding-top:14px;padding-bottom:16px}
.step-two h2,.step-two p{color:var(--white)}
.step-two p{margin-top:9px}
.step-two em{font-style:italic}
.step-three{background:var(--light);padding-top:12px;padding-bottom:12px;margin-top:6px}
.contact-row{display:flex;justify-content:center;gap:26px;font-size:13px;color:var(--navy);padding:9px 0 8px}
.contact-item{display:flex;align-items:center;gap:7px}
.contact-icon{width:16px;height:16px;background:var(--gold);border-radius:2px;display:flex;align-items:center;justify-content:center}
.footer-bar{height:14px;background:var(--navy);flex-shrink:0}
.address{text-align:center;font-size:13px;line-height:1.3;color:var(--ink);padding:8px 0}
.footer-fade{flex:1;background:var(--light)}
</style>
</head>
<body>
<main class="flyer">
  <div class="brand">
    <span class="brand-mark"></span>
    <span class="brand-name">Morvale Commerce Bank</span>
  </div>

  <div class="hero-photo" role="img" aria-label="Photo of the bank branch building with stone and brick facade, reflective windows and trees"></div>

  <svg class="hero-frame" viewBox="0 0 620 360" aria-hidden="true">
    <path d="M292 30 H604" fill="none" stroke="#e2d5bd" stroke-width="2"/>
    <polygon points="30,140 330,140 370,240 330,340 30,340" fill="var(--gold)"/>
    <path d="M30 346 H334 L374 244" fill="none" stroke="var(--gold)" stroke-width="2"/>
  </svg>

  <div class="intro">
    <p>Switching as easy as 1-2-3!</p>
    <p class="intro-lead">One of the main reasons people don't switch banks is that it can be a hassle.</p>
    <p class="intro-lead">At Morvale Commerce Bank we make it easy. We value your time and with our efficient three step process, switching banks has never been easier.</p>
  </div>

  <div class="hero-tag">We look forward to creating an exceptional experience for you at Morvale Commerce Bank.</div>

  <div class="flyer-body">
    <section class="step step-one">
      <h2>1. Open a Morvale Commerce Bank Account</h2>
      <p>Stop by our branch and visit with our knowledgeable team to open your new account. We will be happy to assist you in choosing the right account for your banking needs.</p>
    </section>

    <section class="step step-two">
      <h2>2. Stop using your old account and redirect your automatic payments and direct deposits</h2>
      <p><em>It is important to remember to keep your old account open to ensure all your outstanding checks, deposits, and automatic withdrawals have cleared.</em></p>
      <p>We will provide you with a <strong>Payments Checklist</strong> to help you determine the companies you may need to notify of your account change so they can redirect any deposits or automatic withdrawals.</p>
      <p>Our <strong>Direct Deposit Change Notification</strong> and <strong>Notification of Automatic Withdrawal Change</strong> forms will easily allow companies to redirect your direct deposit(s) and automatic withdrawals to your new Morvale Commerce Bank account.</p>
    </section>

    <section class="step step-three">
      <h2>3. Close your old account</h2>
      <p>Now you are ready to switch. We will even provide an Account Closure Authorization form to close your old account. Any remaining account balance will be transferred to your Morvale Commerce Bank account.</p>
    </section>

    <div class="contact-row">
      <span class="contact-item">
        <span class="contact-icon"><svg width="10" height="10" viewBox="0 0 24 24" aria-hidden="true"><path fill="#fff" d="M6.6 10.8a15.1 15.1 0 0 0 6.6 6.6l2.2-2.2c.3-.3.7-.4 1-.2 1.1.4 2.3.6 3.6.6.6 0 1 .4 1 1V20c0 .6-.4 1-1 1A17 17 0 0 1 3 4c0-.6.4-1 1-1h3.5c.6 0 1 .4 1 1 0 1.3.2 2.5.6 3.6.1.3 0 .7-.2 1z"/></svg></span>
        480.555.0147
      </span>
      <span class="contact-item">
        <span class="contact-icon"><svg width="10" height="10" viewBox="0 0 24 24" aria-hidden="true"><path fill="#fff" d="M5 2l14 9-6 1.5 3.5 7-2.5 1.2-3.5-7L6 17z"/></svg></span>
        www.morvalecommercebank.com
      </span>
    </div>
    <div class="footer-bar"></div>
    <p class="address">2740 Desert Crest Avenue, Suite 310<br>Mesa Ridge, AZ 85990</p>
    <div class="footer-fade"></div>
  </div>
</main>
</body>
</html>
```